Career Management Consultant Fun Professional Business Card

This is a business card for a personal career management consultant. The vibe needs to be professional but fun, modern with colour.

The name of the business is "Marcus Telvorne Career Management Consulting"

The name of the individual is "Marcus Telvorne" and his title is "Career Management Consultant"

Contact Information for Business Card

Marcus Telvorne
Phone: 0400 731 862
Email: Marcus.Telvorne@quillmail.net

```html
<!DOCTYPE html>
<html lang="en">
<head>
<meta charset="UTF-8">
<title>Marcus Telvorne – Business Card</title>
<link href="https://fonts.googleapis.com/css2?family=Jost:wght@300;400;800&display=swap" rel="stylesheet">
<style>
  :root {
    --stage: #2b2623;
    --card: #0b0c0d;
    --card-edge: #1c1e20;
    --accent: #27aad6;
    --ink: #ffffff;
    --muted: #c8ccd0;
  }
  * { box-sizing: border-box; margin: 0; padding: 0; }
  html, body {
    width: 1200px; height: 945px; overflow: hidden;
    background: var(--stage);
    font-family: "Jost", "Futura", sans-serif;
  }
  .stage {
    position: relative; width: 1200px; height: 945px;
    display: flex; align-items: center; justify-content: center; gap: 80px;
  }
  .card {
    position: relative;
    background: linear-gradient(160deg, #1a1c1e 0%, var(--card) 45%, #050506 100%);
    border: 1px solid var(--card-edge);
    border-radius: 16px;
    box-shadow: 0 18px 40px rgba(0,0,0,.45);
    overflow: hidden;
  }
  .card-front { width: 300px; height: 540px; }
  .card-back  { width: 540px; height: 300px; }

  /* brand lockup */
  .brand { display: flex; flex-direction: column; align-items: center; }
  .brand-mark {
    display: flex; align-items: center; gap: 10px;
  }
  .brand-dot {
    width: 34px; height: 34px; border-radius: 50%;
    background: var(--accent);
  }
  .brand-name {
    color: var(--ink); font-weight: 800; text-transform: uppercase;
    letter-spacing: .5px; line-height: 1;
  }
  .brand-tagline {
    color: var(--accent); font-weight: 400; text-transform: uppercase;
    letter-spacing: 1.2px;
  }

  /* front card */
  .card-front .brand { position: absolute; top: 70px; left: 0; right: 0; }
  .card-front .brand-name { font-size: 19px; }
  .card-front .brand-tagline { font-size: 8.5px; margin-top: 10px; }

  .person {
    position: absolute; top: 262px; left: 28px; right: 28px;
  }
  .person-name {
    color: var(--ink); font-weight: 800; font-size: 22px;
    text-transform: uppercase; letter-spacing: .5px;
    padding: 8px 0 8px;
    border-top: 2px solid var(--muted);
    border-bottom: 2px solid var(--muted);
    text-align: center;
  }
  .person-title {
    color: var(--accent); font-size: 9px; letter-spacing: 1.2px;
    text-transform: uppercase; text-align: center; margin-top: 8px;
  }
  .contacts {
    list-style: none; margin-top: 22px;
    display: flex; flex-direction: column; gap: 10px;
  }
  .contact {
    display: flex; align-items: center; gap: 9px;
    color: var(--accent); font-weight: 300; font-size: 12px;
    letter-spacing: .6px; text-transform: uppercase;
  }
  .contact-icon {
    width: 16px; height: 16px; flex: none;
  }

  /* back card */
  .card-back .brand {
    position: absolute; inset: 0; justify-content: center;
  }
  .card-back .brand-dot { width: 52px; height: 52px; }
  .card-back .brand-name { font-size: 30px; }
  .card-back .brand-tagline { font-size: 11px; margin-top: 12px; }
</style>
</head>
<body>
<main class="stage">

  <article class="card card-front">
    <header class="brand">
      <div class="brand-mark">
        <span class="brand-dot"></span>
        <span class="brand-name">Marcus Telvorne</span>
      </div>
      <p class="brand-tagline">Career Management Consulting</p>
    </header>

    <section class="person">
      <h1 class="person-name">Marcus Telvorne</h1>
      <p class="person-title">Career Management Consultant</p>
      <ul class="contacts">
        <li class="contact">
          <svg class="contact-icon" viewBox="0 0 16 16" aria-hidden="true">
            <rect x="0.5" y="0.5" width="15" height="15" rx="3" fill="none" stroke="var(--accent)"/>
            <path d="M6 4.2c-.4 0-1.4.6-1.4 1.5 0 2.6 3 5.7 5.7 5.7.9 0 1.5-1 1.5-1.4l-1.6-1.1-.9.8c-1-.4-2.1-1.5-2.5-2.5l.8-.9z" fill="var(--accent)"/>
          </svg>
          <span>0400 731 862</span>
        </li>
        <li class="contact">
          <svg class="contact-icon" viewBox="0 0 16 16" aria-hidden="true">
            <rect x="0.5" y="0.5" width="15" height="15" rx="3" fill="none" stroke="var(--accent)"/>
            <rect x="3.5" y="5" width="9" height="6" fill="none" stroke="var(--accent)"/>
            <path d="M3.5 5l4.5 3.5L12.5 5" fill="none" stroke="var(--accent)"/>
          </svg>
          <span>Marcus.Telvorne@quillmail.net</span>
        </li>
      </ul>
    </section>
  </article>

  <article class="card card-back">
    <div class="brand">
      <div class="brand-mark">
        <span class="brand-dot"></span>
        <span class="brand-name">Marcus Telvorne</span>
      </div>
      <p class="brand-tagline">Career Management Consulting</p>
    </div>
  </article>

</main>
</body>
</html>
```